Homecare Information Flyer

We require a brochure/ leaflet to be created which would provide healthcare information to our staff and patients on the topic of- Pressure Ulcers. The document would ideally be 3 fold. It should include our Logo/ Company Information (Marrowby Staffing).

I have attached-
- Logo
- Text/ Visual images to be included.

Industry/Entity Type

Healthcare

```html
<!DOCTYPE html>
<html lang="en">
<head>
<meta charset="utf-8">
<title>Pressure Ulcers – Information Leaflet</title>
<link href="https://fonts.googleapis.com/css2?family=Arimo:wght@400;700&display=swap" rel="stylesheet">
<style>
:root{
  --ink:#2b2b2b;
  --green-dark:#3d7f34;
  --green-head:#4a8a3c;
  --bar-light:#eef4cf;
  --bar-mid:#c9dc6a;
  --bar-strong:#a9c83c;
  --white:#ffffff;
  --arrow:#b6cf4a;
  --figure:#d9d9d9;
  --figure-warm:#f3dcc0;
  --ring:#e08a8a;
}
*{margin:0;padding:0;box-sizing:border-box}
html,body{width:1200px;height:927px;overflow:hidden;background:var(--white)}
body{font-family:"Arimo",Arial,sans-serif;color:var(--ink)}
.leaflet{position:relative;width:1200px;height:927px}
.panel{position:absolute;top:0;height:927px}
.panel--left{left:12px;width:390px}
.panel--middle{left:412px;width:380px}
.panel--right{left:797px;width:392px}

.title-bar{
  background:linear-gradient(90deg,var(--bar-light) 0%,var(--bar-mid) 55%,var(--bar-strong) 100%);
  padding:4px 8px 3px;
  font-weight:700;font-size:25px;letter-spacing:1.6px;line-height:1.2;
  color:var(--green-dark);
}
.title-bar .accent{color:var(--white)}
.lead{font-size:15.5px;line-height:1.38;padding:0 10px}
.topic{
  font-weight:700;font-size:26px;letter-spacing:1.4px;color:var(--green-head);
  line-height:1.15;padding:0 10px;
}
.topic--middle{padding:0 10px 0 0;font-size:25px}
.text{font-size:15.5px;line-height:1.36;padding:0 10px}
.panel--middle .text{padding:0}

.signs{list-style:none;font-size:15.5px;line-height:1.5;padding-left:10px}
.signs li{display:flex;align-items:center}
.signs svg{width:26px;height:16px;margin-right:12px;flex:none}
.signs .plain{padding-left:54px}

.pose-label{position:absolute;font-size:14px}
.figure{position:absolute;border-radius:30px;background:linear-gradient(180deg,#f4f4f4,var(--figure))}
.part{position:absolute;font-size:11px;font-weight:700;text-align:center;line-height:1.1}
.chair-scene{
  position:absolute;left:33px;top:648px;width:322px;height:252px;border-radius:8px;
  background:radial-gradient(ellipse at 45% 45%,var(--figure-warm) 0%,#f7eee4 45%,#eeeeee 100%);
  box-shadow:0 0 6px rgba(0,0,0,.25);
}
</style>
</head>
<body>
<main class="leaflet">

  <section class="panel panel--left">
    <h2 class="title-bar" style="margin-top:33px">What is a <span class="accent">Pressure Ulcer?</span></h2>
    <p class="lead" style="margin-top:8px">A pressure ulcer is an area of damage to the skin and underlying tissue.<br>They are sometimes known as pressure sores or bed sores.</p>

    <h2 class="title-bar" style="margin-top:40px">What causes a <span class="accent">Pressure Ulcer?</span></h2>
    <p class="lead" style="margin-top:6px;padding-right:120px">Pressure ulcers are caused by poor circulation to tissues due to a combination of the following factors:</p>

    <h3 class="topic" style="margin-top:14px">Pressure</h3>
    <p class="text">Body weight and some equipment (e.g. anti-thrombosis stockings) can squash the skin and other tissues where parts are under pressure. This reduces the blood supply to the area and can lead to tissue damage.</p>
    <h3 class="topic" style="margin-top:4px">Shearing</h3>
    <p class="text">Sliding or slumping down the bed/chair can damage the skin and deeper layers of tissue.</p>
    <h3 class="topic" style="margin-top:4px">Friction</h3>
    <p class="text">Poor moving and handling methods can remove the top layers of skin. Repeated friction can increase your risk.</p>

    <h2 class="title-bar" style="margin-top:26px">Who is most at risk of<br>Developing <span class="accent">Pressure Ulcers?</span></h2>
    <p class="lead" style="margin-top:10px">You may be at risk of developing pressure ulcers for a number of reasons including the following:</p>
    <h3 class="topic" style="margin-top:16px">Problems with Movement</h3>
    <p class="text">If your ability to move is limited you don't get enough oxygen to the parts under pressure</p>
  </section>

  <section class="panel panel--middle">
    <h3 class="topic topic--middle" style="margin-top:20px">Poor Circulation</h3>
    <p class="text">Vascular disease or smoking reduces your circulation</p>
    <h3 class="topic topic--middle" style="margin-top:20px">Moist Skin</h3>
    <p class="text">You may be at increased risk if your skin is too damp, due to incontinence, sweat or a weeping wound. It is important that your skin is kept clean and healthy.</p>
    <h3 class="topic topic--middle" style="margin-top:20px">Lack of Sensitivity to Pain of Discomfort</h3>
    <p class="text">Conditions such as Diabetes Stroke, Nerve, Muscle Disorders, etc. reduce the normal sensations that usually prompt you, or enable you to move. Some treatments (e.g. Epidural pain relief, medications, and operations) reduce your sensitivity to pain or discomfort so that you are not aware of the need to move.</p>
    <h3 class="topic topic--middle" style="margin-top:20px">Previous Tissue Damage</h3>
    <p class="text">Scar tissue will have lost some of its previous strength and is more prone to breakdown.</p>
    <h3 class="topic topic--middle" style="margin-top:20px">Inadequate Diet of Fluid Intake</h3>
    <p class="text">Lack of fluid may dehydrate your tissues. Weight gain or loss can affect the pressure distribution over bony points and healing.</p>
    <h3 class="topic topic--middle" style="margin-top:20px">Risk Assessment</h3>
    <p class="text">To assess your risk of developing Pressure Ulcers, a member of your Health Care team will examine/assess you and ask you some questions. This will help to identify if you require specialised equipment or other forms of care, and will assist in providing for your individual needs.</p>
  </section>

  <section class="panel panel--right">
    <h2 class="title-bar" style="margin-top:33px">What are the Early Signs<br>of a <span class="accent">Pressure Ulcer?</span></h2>
    <p class="lead" style="margin-top:8px">You will notice the following signs:</p>
    <ul class="signs">
      <li class="plain">Change in skin colour redder or darker</li>
      <li><svg viewBox="0 0 26 16"><path d="M1 5h14V1l10 7-10 7v-4H1z" fill="none" stroke="var(--arrow)" stroke-width="1.6"/></svg>Heat or cold</li>
      <li><svg viewBox="0 0 26 16"><path d="M1 5h14V1l10 7-10 7v-4H1z" fill="none" stroke="var(--arrow)" stroke-width="1.6"/></svg>Discomfort or pain</li>
      <li><svg viewBox="0 0 26 16"><path d="M1 5h14V1l10 7-10 7v-4H1z" fill="none" stroke="var(--arrow)" stroke-width="1.6"/></svg>Blistering</li>
      <li><svg viewBox="0 0 26 16"><path d="M1 5h14V1l10 7-10 7v-4H1z" fill="none" stroke="var(--arrow)" stroke-width="1.6"/></svg>Skin damage</li>
    </ul>
    <p class="lead" style="padding-right:4px">Without appropriate intervention the damage may worsen, developing into hard black tissue or an open wound.</p>

    <h2 class="title-bar" style="position:absolute;top:307px;left:0;width:392px">Common Locations of<br><span class="accent">Pressure Ulcers</span></h2>

    <p class="pose-label" style="left:18px;top:384px">Laying on your back</p>
    <div class="figure" role="img" aria-label="Outline of a person lying on their back with pressure points marked" style="left:10px;top:418px;width:375px;height:36px"></div>
    <span class="part" style="left:4px;top:462px;width:50px">Back of<br>head</span>
    <span class="part" style="left:64px;top:468px;width:50px">Shoulder<br>blade</span>
    <span class="part" style="left:112px;top:462px;width:40px">Elbow</span>
    <span class="part" style="left:170px;top:462px;width:80px">Cocyx, base of<br>spine</span>
    <span class="part" style="left:318px;top:462px;width:40px">Heel</span>

    <p class="pose-label" style="left:272px;top:510px">Laying on your side</p>
    <div class="figure" role="img" aria-label="Outline of a person lying on their side with pressure points marked" style="left:10px;top:505px;width:375px;height:62px"></div>
    <span class="part" style="left:0;top:548px;width:40px">Ear</span>
    <span class="part" style="left:56px;top:570px;width:70px">Shoulder &amp;<br>upper arm</span>
    <span class="part" style="left:124px;top:568px;width:40px">Elbow</span>
    <span class="part" style="left:176px;top:568px;width:30px">Hip</span>
    <span class="part" style="left:228px;top:546px;width:40px">Thigh</span>
    <span class="part" style="left:276px;top:562px;width:40px">Lower<br>leg</span>
    <span class="part" style="left:332px;top:562px;width:50px">Heel &amp;<br>ankle</span>

    <p class="pose-label" style="left:64px;top:617px">Sitting in a chair</p>
    <div class="chair-scene" role="img" aria-label="Illustration of a person seated in a wheelchair with scapula, elbow, sacrum, ischium, ball of foot and heel marked"></div>
  </section>

</main>
</body>
</html>
```